Marlow Law Stationery - Letterhead, Envelopes, Business Cards

We need high quality business stationery for our Personal Injury Law Firm located in Houston, Texas. The design should include the logo, Marlow Law Group, PLLC, 713-555-4718, 2150 Fernbrook Avenue, Suite 310, Houston, Texas 77019 www.MarlowLaw.example. The colors are blue and white. The letterhead should also include the Attorneys - Tessa Quill, Mitchell R. Marlow and Derek Hale.

```html
<!DOCTYPE html>
<html lang="en">
<head>
<meta charset="utf-8">
<title>Marlow Law Stationery</title>
<link href="https://fonts.googleapis.com/css2?family=Open+Sans:wght@400;700&family=Poppins:wght@400;600;700&display=swap" rel="stylesheet">
<style>
  :root {
    --navy: #0e1b3f;
    --white: #ffffff;
    --ink: #4a4f5a;
    --rule: #9aa0aa;
    --backdrop: #26292c;
    --label: #ffffff;
  }
  * { box-sizing: border-box; margin: 0; padding: 0; }
  html, body { width: 1006px; height: 1200px; overflow: hidden; }
  body {
    position: relative;
    background: radial-gradient(ellipse at 40% 40%, #303437 0%, var(--backdrop) 60%, #1c1e20 100%);
    font-family: "Poppins", sans-serif;
    color: var(--ink);
  }
  .piece-label {
    position: absolute;
    font-family: "Open Sans", sans-serif;
    color: var(--label);
    font-size: 18px;
    font-weight: 400;
    letter-spacing: 0.2px;
  }
  .piece-label--bold { font-weight: 700; }
  .sheet { position: absolute; }

  /* brand mark: plain circle beside the firm name */
  .mark { position: absolute; display: flex; align-items: center; gap: 6px; }
  .mark__dot { border-radius: 50%; background: var(--navy); flex: none; }
  .mark__name {
    font-family: "Poppins", sans-serif;
    font-weight: 600;
    color: var(--navy);
    white-space: nowrap;
  }
  .mark--light .mark__dot { background: var(--white); }
  .mark--light .mark__name { color: var(--white); }

  .contact { position: absolute; font-size: 7px; line-height: 1.35; color: var(--ink); }
  .contact__row { display: flex; align-items: center; gap: 4px; }
  .contact__gap { height: 7px; }
  .contact__firm { font-weight: 600; color: var(--navy); }
  .icon { width: 7px; height: 7px; flex: none; }

  /* business cards */
  .card { width: 380px; height: 217px; }
  .card--front {
    left: 60px; top: 78px;
    background: linear-gradient(135deg, #ffffff 0%, #eceef1 100%);
    border: 5px solid var(--navy);
  }
  .card--back {
    left: 120px; top: 312px;
    background: var(--navy);
    border: 5px solid var(--navy);
  }
  .card--back::before {
    content: ""; position: absolute; inset: 5px;
    border: 3px solid var(--white);
  }
  .card__person { position: absolute; left: 26px; top: 64px; color: var(--white); }
  .card__name { font-weight: 700; font-size: 12px; letter-spacing: 0.5px; text-transform: uppercase; }
  .card__role { font-size: 8.5px; margin-top: 1px; }
  .card__divider { width: 40px; height: 1px; background: var(--white); margin-top: 8px; opacity: 0.8; }
  .card__contact { left: 26px; top: 116px; color: var(--white); font-size: 8.5px; }

  /* note pad */
  .notepad {
    left: 578px; top: 169px; width: 330px; height: 232px;
    background: var(--navy); padding: 5px;
  }
  .notepad__paper { position: relative; width: 100%; height: 100%; background: var(--white); }
  .notepad__paper::before {
    content: ""; position: absolute; inset: 5px; border: 2px solid var(--navy);
  }
  .notepad__line { position: absolute; height: 1px; background: var(--rule); }

  /* letterhead */
  .letterhead {
    left: 580px; top: 568px; width: 395px; height: 514px;
    background: var(--white); border: 4px solid var(--navy);
  }
  .letterhead::before {
    content: ""; position: absolute; inset: 3px; border: 2px solid var(--navy);
  }
  .letterhead__team { position: absolute; right: 17px; bottom: 13px; text-align: right; }
  .member { margin-top: 6px; }
  .member__name { font-weight: 700; font-size: 8.5px; color: var(--navy); text-transform: uppercase; }
  .member__role { font-size: 7.5px; color: var(--ink); line-height: 1.2; }

  /* envelopes */
  .envelope-front {
    left: 55px; top: 638px; width: 407px; height: 173px;
    background: var(--white); border: 2px solid var(--navy);
  }
  .envelope-front::before {
    content: ""; position: absolute; inset: 2px; border: 2px solid var(--navy);
  }
  .envelope-back {
    left: 55px; top: 905px; width: 407px; height: 176px;
    background: var(--white);
  }
  .envelope-back svg { position: absolute; left: 0; top: 0; }
</style>
</head>
<body>

  <div class="piece-label piece-label--bold" style="left:82px; top:40px;">Business Card_3</div>

  <div class="sheet card card--front">
    <div class="mark" style="left:112px; top:86px; gap:9px;">
      <span class="mark__dot" style="width:32px; height:32px;"></span>
      <span class="mark__name" style="font-size:21px;">Marlow Law</span>
    </div>
  </div>

  <div class="sheet card card--back">
    <div class="card__person">
      <div class="card__name">Tessa Quill</div>
      <div class="card__role">Managing Partner</div>
      <div class="card__divider"></div>
    </div>
    <div class="contact card__contact">
      <div>2150 Fernbrook Avenue</div>
      <div>Suite 310, Houston, Texas 77019</div>
      <div class="contact__gap"></div>
      <div class="contact__row">
        <svg class="icon" viewBox="0 0 10 10"><path d="M2 1l2 2-1 1.2c.6 1.2 1.6 2.2 2.8 2.8L7 6l2 2-1.3 1.3C4.5 9 1 5.5.7 2.3z" fill="#fff"/></svg>
        <span>713-555-4718</span>
      </div>
      <div class="contact__row">
        <svg class="icon" viewBox="0 0 10 10" fill="none" stroke="#fff" stroke-width="1"><circle cx="5" cy="5" r="4"/><ellipse cx="5" cy="5" rx="1.8" ry="4"/><path d="M1 5h8"/></svg>
        <span>www.MarlowLaw.example</span>
      </div>
    </div>
    <div class="mark mark--light" style="left:228px; top:86px; gap:7px;">
      <span class="mark__dot" style="width:22px; height:22px;"></span>
      <span class="mark__name" style="font-size:16px;">Marlow Law</span>
    </div>
  </div>

  <div class="piece-label" style="left:578px; top:134px;">Note Pads_3</div>
  <div class="sheet notepad">
    <div class="notepad__paper">
      <div class="notepad__line" style="left:19px; top:45px; width:212px;"></div>
      <div class="notepad__line" style="left:19px; top:61px; width:221px;"></div>
      <div class="notepad__line" style="left:19px; top:77px; width:226px;"></div>
      <div class="notepad__line" style="left:19px; top:93px; width:292px;"></div>
      <div class="notepad__line" style="left:19px; top:109px; width:292px;"></div>
      <div class="notepad__line" style="left:19px; top:125px; width:292px;"></div>
      <div class="notepad__line" style="left:19px; top:141px; width:292px;"></div>
      <div class="notepad__line" style="left:19px; top:157px; width:292px;"></div>
      <div class="notepad__line" style="left:137px; top:173px; width:174px;"></div>
      <div class="notepad__line" style="left:137px; top:189px; width:174px;"></div>
      <div class="notepad__line" style="left:137px; top:205px; width:174px;"></div>
      <div class="mark" style="right:16px; top:24px; gap:4px; flex-direction:column;">
        <span class="mark__dot" style="width:26px; height:26px;"></span>
        <span class="mark__name" style="font-size:9px;">Marlow Law</span>
      </div>
      <div class="contact" style="left:19px; top:160px; font-size:6.5px;">
        <div>2150 Fernbrook Avenue</div>
        <div>Suite 310, Houston, Texas 77019</div>
        <div class="contact__gap"></div>
        <div class="contact__row">
          <svg class="icon" viewBox="0 0 10 10"><path d="M2 1l2 2-1 1.2c.6 1.2 1.6 2.2 2.8 2.8L7 6l2 2-1.3 1.3C4.5 9 1 5.5.7 2.3z" fill="#0e1b3f"/></svg>
          <span>713-555-4718</span>
        </div>
        <div class="contact__row">
          <svg class="icon" viewBox="0 0 10 10" fill="none" stroke="#0e1b3f" stroke-width="1"><circle cx="5" cy="5" r="4"/><ellipse cx="5" cy="5" rx="1.8" ry="4"/><path d="M1 5h8"/></svg>
          <span>www.MarlowLaw.example</span>
        </div>
      </div>
    </div>
  </div>

  <div class="piece-label" style="left:578px; top:529px;">Letterhead_3</div>
  <div class="sheet letterhead">
    <div class="mark" style="left:297px; top:22px; gap:4px; flex-direction:column;">
      <span class="mark__dot" style="width:34px; height:34px;"></span>
      <span class="mark__name" style="font-size:13px;">Marlow Law</span>
    </div>
    <div class="contact" style="left:14px; bottom:15px; font-size:7.5px;">
      <div class="contact__firm">Marlow Law Group, PLLC</div>
      <div>2150 Fernbrook Avenue</div>
      <div>Suite 310, Houston, Texas 77019</div>
      <div class="contact__gap" style="height:10px;"></div>
      <div class="contact__row">
        <svg class="icon" viewBox="0 0 10 10"><path d="M2 1l2 2-1 1.2c.6 1.2 1.6 2.2 2.8 2.8L7 6l2 2-1.3 1.3C4.5 9 1 5.5.7 2.3z" fill="#0e1b3f"/></svg>
        <span>713-555-4718</span>
      </div>
      <div class="contact__row">
        <svg class="icon" viewBox="0 0 10 10" fill="none" stroke="#0e1b3f" stroke-width="1"><circle cx="5" cy="5" r="4"/><ellipse cx="5" cy="5" rx="1.8" ry="4"/><path d="M1 5h8"/></svg>
        <span>www.MarlowLaw.example</span>
      </div>
    </div>
    <div class="letterhead__team">
      <div class="member"><div class="member__name">Mitchell R. Marlow</div><div class="member__role">Founding partner / Attorney</div></div>
      <div class="member"><div class="member__name">Tessa Quill</div><div class="member__role">Managing Partner / Associate Attorney</div></div>
      <div class="member"><div class="member__name">Derek Hale</div><div class="member__role">Associate Attorney</div></div>
    </div>
  </div>

  <div class="piece-label" style="left:55px; top:596px;">ENV Front_3</div>
  <div class="sheet envelope-front">
    <div class="mark" style="left:13px; top:12px; gap:3px; flex-direction:column;">
      <span class="mark__dot" style="width:30px; height:30px;"></span>
      <span class="mark__name" style="font-size:11px;">Marlow Law</span>
    </div>
    <div class="contact" style="left:13px; bottom:8px; font-size:7px;">
      <div>2150 Fernbrook Avenue</div>
      <div>Suite 310, Houston, Texas 77019</div>
    </div>
  </div>

  <div class="piece-label" style="left:55px; top:865px;">ENV Back_3</div>
  <div class="sheet envelope-back">
    <svg width="407" height="176" viewBox="0 0 407 176" aria-hidden="true">
      <path d="M0 0 L14 26 Q20 36 34 38 L196 63 Q203 65 210 63 L373 38 Q387 36 393 26 L407 0" fill="none" stroke="#0e1b3f" stroke-width="3"/>
      <path d="M3 0 L16 23 Q22 32 35 34 L196 59 Q203 61 210 59 L372 34 Q385 32 391 23 L404 0" fill="none" stroke="#0e1b3f" stroke-width="0.8"/>
    </svg>
    <div class="mark" style="left:174px; top:17px; gap:4px;">
      <span class="mark__dot" style="width:14px; height:14px;"></span>
      <span class="mark__name" style="font-size:9px;">Marlow Law</span>
    </div>
  </div>

</body>
</html>
```